Buffet Restaurant A0 poster for pavement A Board

We are an 'All you can eat' buffet restaurant in a large competitive shopping mall in the UK. We need a size A0 poster for an 'A board' to stand outside our restaurant on the mall to attract customers. The minimum it has to say is that the price is £9.99. Simple!

Please note: the shop front sign on the photos is not blue, it white led backlit that looks blue on photo. Also logo is very simple text you can see on sign. Also check out tallfernos.net

Target Market(s)

Passers by (see Quaybridge demographic via google search)

Industry/Entity Type

Restaurant

Font styles to use
Sans Serif

Requirements
Must have
• Must do the job of enticing customers to our door

```html
<!DOCTYPE html>
<html lang="en">
<head>
<meta charset="utf-8">
<title>Tall Fernos World Buffet – All you can eat for £9.99</title>
<link rel="stylesheet" href="https://fonts.googleapis.com/css2?family=Arimo:ital,wght@0,400;0,700;1,400&family=Pacifico&family=Great+Vibes&family=Archivo+Black&display=swap">
<style>
  :root {
    --board-dark: #141414;
    --board-mid: #262626;
    --chalk-faint: rgba(255,255,255,0.06);
    --ink: #ffffff;
    --gold: #b5841e;
    --muted: #e6e6e6;
  }
  * { margin: 0; padding: 0; box-sizing: border-box; }
  html, body { width: 849px; height: 1200px; overflow: hidden; background: var(--board-dark); }
  .poster {
    position: relative; width: 849px; height: 1200px; overflow: hidden;
    background: linear-gradient(180deg, var(--board-mid) 0%, #1c1c1c 45%, var(--board-dark) 100%);
    color: var(--ink); font-family: "Arimo", Arial, sans-serif;
  }
  .poster > * { position: absolute; }
  .decor { left: 0; top: 0; width: 849px; height: 1200px; }
  .chalk-art { left: 48px; top: 468px; width: 754px; height: 682px;
    background: radial-gradient(ellipse at 40% 55%, var(--chalk-faint), rgba(255,255,255,0.02) 70%); }
  .tagline { left: 0; width: 849px; top: 42px; text-align: center;
    font-family: "Pacifico", cursive; font-size: 22px; letter-spacing: 0.3px; }
  .cuisines { left: 0; width: 849px; top: 334px; text-align: center;
    font-weight: 700; font-size: 14px; letter-spacing: 1px; }
  .offer-lead { left: 0; width: 849px; top: 412px; text-align: center;
    font-family: "Pacifico", cursive; font-size: 42px; }
  .menu-label { left: 94px; top: 850px; font-family: "Great Vibes", cursive; font-size: 40px; }
  .service-day { top: 912px; text-align: center;
    font-family: "Archivo Black", sans-serif; font-size: 33px; letter-spacing: -0.5px;
    transform: skewX(-6deg); text-shadow: 2px 2px 0 #555, 3px 3px 0 #000; }
  .service-day--weekdays { left: 150px; width: 228px; }
  .service-day--weekends { left: 486px; width: 240px; }
  .service-day sup { font-size: 24px; vertical-align: 10px; }
  .service-hours { font-size: 11px; color: var(--muted); text-align: center; line-height: 1.3; }
  .service-hours--weekdays { left: 166px; top: 958px; width: 196px; }
  .service-hours--weekends { left: 488px; top: 956px; width: 230px; }
  .price-note { font-weight: 700; font-size: 20px; top: 1033px; }
  .price-note--children { left: 108px; }
  .price-note--babies { left: 466px; }
  .holiday-note { right: 74px; top: 1113px; font-style: italic; font-size: 15px; }
  .holiday-note span { color: var(--gold); }
</style>
</head>
<body>
<main class="poster">
  <div class="chalk-art" role="img" aria-label="Faint chalk-drawn food doodles with the words pizza, passion, fresh and friends"></div>

  <svg class="decor" viewBox="0 0 849 1200">
    <!-- restaurant name, set plainly in one weight -->
    <text class="brand-name" x="424.5" y="222" text-anchor="middle" textLength="740" lengthAdjust="spacingAndGlyphs"
          font-family="Arimo, Arial, sans-serif" font-weight="700" font-size="132" fill="var(--ink)">TALL FERNOS</text>
    <text class="brand-subtitle" x="424.5" y="304" text-anchor="middle" letter-spacing="4"
          font-family="Arimo, Arial, sans-serif" font-weight="700" font-size="40" fill="var(--ink)">WORLD BUFFET</text>

    <!-- double frame with gap for headline -->
    <g fill="none" stroke="var(--ink)" stroke-width="1.5">
      <path d="M225 450 H38 V1162 H812 V450 H625"/>
      <path d="M225 456 H44 V1156 H806 V456 H625"/>
    </g>

    <!-- main price roundel -->
    <circle cx="424" cy="670" r="178" fill="var(--gold)"/>
    <circle cx="424" cy="670" r="163" fill="none" stroke="var(--ink)" stroke-width="2"/>
    <text class="main-price" x="424" y="710" text-anchor="middle"
          font-family="Arimo, Arial, sans-serif" font-weight="700" font-size="112" fill="var(--ink)">£9.99</text>

    <!-- dotted leaders -->
    <g stroke="var(--ink)" stroke-width="2" stroke-dasharray="1.5 3.5" stroke-linecap="round">
      <line x1="104" y1="965" x2="164" y2="965"/>
      <line x1="418" y1="965" x2="432" y2="965"/>
      <line x1="722" y1="965" x2="774" y2="965"/>
    </g>

    <!-- small price badges -->
    <g class="price-badge">
      <circle cx="350" cy="1046" r="33" fill="var(--gold)"/>
      <circle cx="350" cy="1046" r="29" fill="none" stroke="var(--ink)" stroke-width="2"/>
      <text x="350" y="1052" text-anchor="middle" font-family="Arimo, Arial, sans-serif" font-weight="700" font-size="16" fill="var(--ink)">£4.50</text>
    </g>
    <g class="price-badge">
      <circle cx="740" cy="1046" r="33" fill="var(--gold)"/>
      <circle cx="740" cy="1046" r="29" fill="none" stroke="var(--ink)" stroke-width="2"/>
      <text x="740" y="1052" text-anchor="middle" font-family="Arimo, Arial, sans-serif" font-weight="700" font-size="16" fill="var(--ink)">£1.99</text>
    </g>
  </svg>

  <p class="tagline">Generous plates for every appetite, seven days a week</p>
  <p class="cuisines">AMERICAN - ITALIAN - BRITISH - INDIAN - CHINESE</p>
  <p class="offer-lead">All you can eat for</p>

  <p class="menu-label">Our menu</p>
  <h2 class="service-day service-day--weekdays">WEEKDAYS</h2>
  <h2 class="service-day service-day--weekends">WEEKENDS<sup>*</sup></h2>
  <p class="service-hours service-hours--weekdays">From 11:15 am until shops close</p>
  <p class="service-hours service-hours--weekends">From 11:15 am until 9:30 pm Saturdays<br>and 6pm Sundays</p>

  <p class="price-note price-note--children">Children under 11</p>
  <p class="price-note price-note--babies">Babies in high-chairs</p>
  <p class="holiday-note"><span>*</span>and public holidays</p>
</main>
</body>
</html>
```